Full color cover for Chamber's Membership Menu

I need a cover, 8 1/2" x 11" for our Chamber of Commerce Membership Menu. Is should have our logo and the words, Membership Menu on it. That's all that is necessary but it can include one or more of the other photos (maybe a college?) that I added, though they are not required. Our logo colors should be used: 37-170-226, 58-181-74, 40-56-144, 247-148-29, 189-190-192.

Target Market(s)

Business owners and managers

Industry/Entity Type

Business Development

Font styles to use
Serif

Colors
0054AA
0677BA
7BADD7
CADEEF
E8F1F8
00AB8E
00BBA5
67D7C9
C6EFE9
E9F9F6
F0912C
F2A743
F7CA91
FBE8D2
FDF5EE

Requirements
Must have
• Our logo and the words Membership Menu
Nice to have
• An attractive business-like feel. It can be very simple.

```html
<!DOCTYPE html>
<html lang="en">
<head>
<meta charset="utf-8">
<title>Membership Menu – Cover</title>
<link href="https://fonts.googleapis.com/css2?family=Tinos:wght@400;700&display=swap" rel="stylesheet">
<style>
  :root {
    --page-bg: #d6d6d7;
    --paper: #ffffff;
    --title-blue: #3f4fae;
    --brand-orange: #f5a53c;
    --brand-blue: #3f4fae;
    --brand-gray: #bdbec0;
    --brand-cyan: #3fbde6;
    --mist: #e8f1f8;
    --mist-deep: #cadeef;
    --photo-warm: #9a8a78;
    --photo-dark: #5b4a3e;
    --photo-street: #8c7f7a;
    --photo-store: #7d8a90;
  }
  * { margin: 0; padding: 0; box-sizing: border-box; }
  html, body {
    width: 1200px; height: 1200px; overflow: hidden;
    background: var(--page-bg);
  }
  .cover {
    position: absolute; left: 175px; top: 50px;
    width: 850px; height: 1100px;
    background: var(--paper);
    overflow: hidden;
    box-shadow: 0 6px 24px rgba(0,0,0,0.12);
  }
  .cover__backdrop { position: absolute; inset: 0; }
  .cover__title {
    position: absolute; left: 150px; top: 120px;
    font-family: "Tinos", "Times New Roman", serif;
    font-weight: 400; font-size: 84px; line-height: 0.95;
    color: var(--title-blue); letter-spacing: 2px;
    text-transform: uppercase;
  }
  .cover__title span { display: block; }
  .cover__title .line-two { padding-left: 70px; }
  .band { position: absolute; top: 400px; height: 190px; }
  .band--orange { left: 0; width: 150px; background: var(--brand-orange); }
  .band--blue { left: 150px; width: 100px; background: var(--brand-blue); }
  .band--gray { left: 250px; width: 25px; background: var(--brand-gray); }
  .band--cyan { left: 275px; width: 145px; background: var(--brand-cyan); }
  .photo { position: absolute; }
  .photo--ribbon-street {
    left: 705px; top: 290px; width: 145px; height: 185px;
    background: linear-gradient(160deg, #b7a9a0, var(--photo-street) 60%, #6f6a70);
  }
  .photo--staff-aprons {
    left: 430px; top: 380px; width: 265px; height: 195px;
    background: linear-gradient(170deg, #a88f76, var(--photo-dark) 70%, #3a322d);
  }
  .photo--office-welcome {
    left: 0; top: 600px; width: 420px; height: 190px;
    background: linear-gradient(180deg, #e9e4de, #c7b3a0 55%, var(--photo-warm));
  }
  .photo--ribbon-store {
    left: 430px; top: 585px; width: 340px; height: 205px;
    background: linear-gradient(170deg, #8fa3a8, var(--photo-store) 50%, #6e5f62);
  }
  .brand {
    position: absolute; left: 330px; top: 880px;
    display: flex; align-items: center; gap: 16px;
  }
  .brand__dot {
    width: 54px; height: 54px; border-radius: 50%;
    background: var(--brand-cyan);
  }
  .brand__name {
    font-family: "Tinos", "Times New Roman", serif;
    font-weight: 700; color: var(--brand-blue);
    text-transform: uppercase; line-height: 1.05;
  }
  .brand__name .primary { display: block; font-size: 36px; letter-spacing: 0.5px; }
  .brand__name .secondary { display: block; font-size: 22px; letter-spacing: 4px; }
</style>
</head>
<body>
  <main class="cover">
    <svg class="cover__backdrop" width="850" height="1100" viewBox="0 0 850 1100" aria-hidden="true">
      <defs>
        <linearGradient id="mistFade" x1="0" y1="0" x2="0" y2="1">
          <stop offset="0" stop-color="#cadeef" stop-opacity="0.9"/>
          <stop offset="1" stop-color="#e8f1f8" stop-opacity="0"/>
        </linearGradient>
        <linearGradient id="floorFade" x1="0" y1="0" x2="0" y2="1">
          <stop offset="0" stop-color="#f4f7fa" stop-opacity="0"/>
          <stop offset="1" stop-color="#eef2f6" stop-opacity="1"/>
        </linearGradient>
      </defs>
      <rect width="850" height="1100" fill="#fbfcfd"/>
      <polygon points="0,0 850,0 850,260 0,330" fill="url(#mistFade)" opacity="0.55"/>
      <polygon points="380,0 850,0 850,180" fill="#cadeef" opacity="0.45"/>
      <polygon points="0,180 520,60 0,300" fill="#e8f1f8" opacity="0.9"/>
      <polygon points="600,0 850,120 850,0" fill="#7badd7" opacity="0.18"/>
      <path d="M0 330 Q 300 240 850 250" stroke="#cadeef" stroke-width="2" fill="none"/>
      <rect y="800" width="850" height="300" fill="url(#floorFade)"/>
    </svg>

    <h1 class="cover__title"><span>Membership</span><span class="line-two">Menu</span></h1>

    <div class="band band--orange"></div>
    <div class="band band--blue"></div>
    <div class="band band--gray"></div>
    <div class="band band--cyan"></div>

    <div class="photo photo--ribbon-street" role="img" aria-label="Photo of a ribbon-cutting group outside a storefront"></div>
    <div class="photo photo--staff-aprons" role="img" aria-label="Photo of restaurant staff in black aprons"></div>
    <div class="photo photo--office-welcome" role="img" aria-label="Photo of two chamber staff members in the office"></div>
    <div class="photo photo--ribbon-store" role="img" aria-label="Photo of a ribbon-cutting celebration inside a store"></div>

    <div class="brand">
      <div class="brand__dot"></div>
      <div class="brand__name">
        <span class="primary">Riverton Chamber</span>
        <span class="secondary">of Commerce &amp; Tourism</span>
      </div>
    </div>
  </main>
</body>
</html>
```